Lena Hartwell Web

Lena Hartwell is a singer/songwriter that has a presence in the market for over 20 years. She currently has a website, lenahartwell.example that needs a major makeover. IT needs to be reorganized to; 1) make it more user friendly; 2) enable multi-languages including; Spanish, French, Russian, Japanese, Chinese and Portuguese; 3) enable purchases online through a storefront of promotional merchandise and music tracks. She has a logo that needs an update, as well as we currently have a business card open on PixelBazaar for input. Working to re-brand, or refresh her brand.

Lena Hartwell is the next Rosa Delmont! She has 5 platinum records, Lumen Award nominations and tours with Harold Prescott globally and is Nora Vandermeer's key backup singer for 12 years.
Updates

Some common questions have come up.  Here is some further input:

1) Colors - No specific color in mind but probably earth tones.  Although at this point we''re completely open.  Mary likes classical style, Russian, French decor.  Paris architecture. Greek, Italian textures, Goddess like symbols from the Roman Empire, or the symbols and pomp of the British monarchy.  One name on tap for the new CD is "Lanterns Over Quiet Water"
2) Example website - I have not found a new one specifically, but what I don''t like about the existing one is it is not easy to navigate.  Needs to be streamlined and easy to navigate with a storefront for merchandise and music downloads.  
3) On Logo - We''re revamping a "Global" merchandise rollout logo.  We''ve also considered possibly modifying the old english "Hartwell" family crest which signifies royalty, but have not explored that too much.  The hexagon yellow logo on her current website, I was thinking of modifying to gold (brushed - or polished?), then taking the LH lettering using a fountain pen type look there the line thickness flows with pressure on the pen, then make the gold look like a pillow, with the letter making an impression into the gold pillow.  This expands to a high quality pin, blinged up broach with diamonds imbedded for example, Global label identity, tee shirts, label tag on fashion clothing etc etc. 
 4) One thing marketing has asked us to build is a routine video blog to reach out to fans in a personal way.  Short clips of daily activity, travel prep for shows, etc. Possibly a signup/fanpage where people get emails sent back whenever anything new is posted, like a video blog, new pics, new events.  A menu to choose what you get updates on. 

Thanks, Dennis

Target Market(s)

1) Fan base in Europe, Asia, Latin America and North America
2) Movie producers seeking soundtracks
3) Private clients seeking an outstanding performer for corporate events

Industry/Entity Type

Singer

Requirements
Must have
• Better organization into smaller pages. Items critical include: 1) music tracks, 2) ClipStream links, 3) photos & Video, 4) storefront to enable online merchandise purchase 5) a way to illustrate her genre from; gospel, to rock, funk, R&B, country,

```html
<!DOCTYPE html>
<html lang="en">
<head>
<meta charset="utf-8">
<title>Lena Hartwell — The Soul of Music</title>
<link rel="stylesheet" href="https://fonts.googleapis.com/css2?family=Ubuntu:wght@300;400;500;700&family=Oswald:wght@500;600&family=Open+Sans:wght@400;600;700&family=Cinzel:wght@400&display=swap">
<style>
:root{
  --bg-deep:#2a1608;
  --bg:#34200d;
  --panel:#4a2c11;
  --panel-soft:#402510;
  --band:#4d2e0c;
  --line:#5e3a16;
  --yellow:#f3c300;
  --gold:#eeb515;
  --gold-dark:#b88406;
  --cream:#f4e6c6;
  --text:#e9dcc0;
  --muted:#bfa57a;
  --white:#ffffff;
  --input:#fbf5e6;
}
*{box-sizing:border-box;margin:0;padding:0}
html,body{width:1200px;height:3278px;overflow:hidden}
body{position:relative;background:linear-gradient(180deg,var(--bg) 0%,#3a230e 40%,#331d0b 75%,var(--bg-deep) 100%);font-family:"Open Sans",Arial,sans-serif;color:var(--text)}
.abs{position:absolute}
.ph{position:absolute;overflow:hidden}
h2,h3{font-weight:500}

/* header */
.site-header{left:0;top:0;width:1200px;height:112px;background:#2b1707;border-bottom:3px solid #1d0f04}
.brand{left:139px;top:36px;display:flex;align-items:center;gap:10px;font:700 20px "Ubuntu",sans-serif;color:var(--yellow)}
.brand-mark{width:26px;height:26px;background:var(--yellow)}
.main-nav{left:442px;top:0;height:112px;display:flex;align-items:center;font:400 16px "Open Sans",sans-serif;color:var(--white)}
.main-nav a{color:var(--white);text-decoration:none;padding:0 12px}
.main-nav .current{background:var(--yellow);height:112px;width:74px;display:flex;align-items:center;justify-content:center;padding:0;margin-right:12px}
.main-nav .pill{background:var(--yellow);border-radius:16px;padding:6px 22px;color:#fff;margin:0 10px}

/* hero */
.hero{left:0;top:112px;width:1200px;height:620px;background:linear-gradient(180deg,#e4b600 0%,#d7a600 55%,#b37c06 100%)}
.hero-photo{right:0;top:0;width:620px;height:620px;background:radial-gradient(ellipse at 55% 40%,#cfa36b 0%,#8f6126 35%,#c79b08 70%,#d4a700 100%)}
.hero-kicker{left:139px;top:178px;font:700 34px "Oswald",sans-serif;color:#4a2a0c;letter-spacing:.5px}
.hero-title{left:139px;top:224px;font:300 62px "Ubuntu",sans-serif;color:#5a3410}
.hero-copy{left:139px;top:300px;width:440px;font:400 14px/21px "Open Sans",sans-serif;color:#4a2a0c}
.hero-arrows{left:139px;top:418px;display:flex;gap:16px}

/* promo boxes */
.promo{top:631px;width:300px;height:180px;background:rgba(74,42,14,.92);border:1px solid #6b4414;padding:18px 18px}
.promo h3{font:600 30px/30px "Oswald",sans-serif;color:var(--white);text-transform:uppercase}
.promo h3 span{color:var(--gold);font-size:19px}
.promo p{font-size:12px;line-height:16px;color:var(--text);margin-top:10px;width:190px}
.promo .go{position:absolute;right:18px;bottom:20px;width:42px;height:42px;border-radius:50%;background:#7c4d12;display:flex;align-items:center;justify-content:center}
.player{position:absolute;left:16px;right:16px;bottom:22px;height:26px;display:flex;align-items:center;gap:8px}
.player .bar{flex:1;height:6px;background:var(--gold-dark);border-radius:3px;position:relative}
.player .knob{position:absolute;left:58%;top:-13px;width:32px;height:32px;border-radius:50%;border:3px solid var(--white);background:#2b1707}

/* section headings */
.sec-title{font:500 27px "Ubuntu",sans-serif;color:var(--white)}
.sec-title em{font-style:normal;color:var(--gold)}

/* stories */
.stories{left:173px;top:917px;width:590px;height:200px;background:var(--panel);border:1px solid var(--line)}
.badge{left:32px;top:32px;width:118px;height:118px;border-radius:50%;background:#fff;border:6px solid #e9e1d4}
.story-title{left:180px;top:22px;font:500 18px "Ubuntu",sans-serif;color:var(--gold)}
.story-copy{left:180px;top:62px;width:390px;font-size:12px;line-height:17px;color:var(--text)}
.mini-arrows{display:flex;gap:6px}
.mini-arrows span{width:18px;height:18px;background:#6a4313;display:flex;align-items:center;justify-content:center}
.magazine{left:785px;top:917px;width:285px;height:200px;background:linear-gradient(160deg,#c9a57a,#6b4421 55%,#2f1a0b)}
.rule{left:154px;top:1147px;width:916px;height:1px;background:var(--line)}

/* album */
.album-panel{left:139px;top:1176px;width:960px;height:408px;background:var(--panel);border:1px solid var(--line)}
.album-copy{left:34px;top:110px;width:180px;font:600 13px/19px "Open Sans",sans-serif;color:var(--white)}
.album{top:53px;width:210px}
.album .cover{position:relative;height:264px;border-top:3px solid var(--yellow);border-bottom:3px solid var(--yellow)}
.album .name{font-size:15px;color:var(--white);margin-top:14px}
.album .meta{display:flex;justify-content:space-between;font-size:10px;color:var(--gold);margin-top:6px}

/* events */
.event-img{left:154px;top:1692px;width:206px;height:185px;background:radial-gradient(ellipse at 50% 45%,#c2883a 0%,#5e3712 45%,#241206 100%)}
.event-text{left:376px;top:1690px;width:205px}
.event-text h4{font:500 15px "Ubuntu",sans-serif;color:var(--gold)}
.event-text p{font-size:12px;line-height:17px;color:var(--text);margin-top:10px}
.event-text .tix{margin-top:48px;font-size:11px;color:var(--gold);display:flex;align-items:center;gap:6px}
.upcoming{left:610px;top:1694px;width:460px;height:166px;background:linear-gradient(90deg,#f0e4cc 0%,#d9c19a 35%,#7c5531 70%,#4a2c12 100%)}
.upcoming .date{position:absolute;left:12px;top:10px;font-size:11px;color:#3b2108}
.upcoming .who{position:absolute;left:12px;top:24px;font:400 40px "Ubuntu",sans-serif;color:#2d1a08}
.upcoming .fan{position:absolute;left:12px;top:74px;font-size:13px;color:#c07d00}
.upcoming .with{position:absolute;left:12px;top:94px;font:500 17px "Ubuntu",sans-serif;color:#3b2108}
.upcoming .venue{position:absolute;left:12px;top:116px;font:500 22px/22px "Ubuntu",sans-serif;color:#d98a00}

/* video */
.video-head{left:154px;top:1927px;width:501px;height:60px;background:var(--yellow);display:flex;align-items:center;gap:14px;padding-left:12px;font:500 27px "Ubuntu",sans-serif;color:#2b1707}
.video-head .ico{width:38px;height:38px;background:#fff;border:3px solid #7a6a4a;display:flex;align-items:center;justify-content:center}
.video-frame{left:154px;top:1987px;width:501px;height:276px;background:radial-gradient(ellipse at 60% 35%,#e0b370 0%,#8a5a22 35%,#2c1707 80%)}
.play{left:160px;top:83px;width:106px;height:106px;border-radius:50%;border:4px solid #fff;display:flex;align-items:center;justify-content:center;background:rgba(0,0,0,.25)}

/* social widget */
.widget{left:691px;top:1927px;width:379px;height:336px;background:var(--panel);border:1px solid var(--line)}
.widget h3{position:absolute;left:30px;top:22px;font:500 27px "Ubuntu",sans-serif;color:var(--gold)}
.widget .find{position:absolute;left:0;top:72px;width:379px;height:36px;border:1px solid var(--gold-dark);padding:7px 28px;font-size:15px;color:var(--gold)}
.widget .profile{position:absolute;left:30px;top:128px;display:flex;gap:14px}
.widget .avatar{width:62px;height:62px;background:var(--yellow);border:3px solid #fff}
.widget .pname{font:400 22px "Open Sans",sans-serif;color:#fff}
.widget .like{display:inline-block;margin-top:4px;font-size:10px;background:#ddd;color:#333;padding:1px 6px}
.widget .sep{position:absolute;left:0;top:216px;width:379px;height:1px;background:var(--line)}
.fans{position:absolute;left:52px;top:238px;display:flex;gap:6px}
.fans i{display:block;width:60px;height:62px;background:linear-gradient(160deg,#cdb6a0,#7a8fb1);border:2px solid #fff}

/* get in touch */
.touch{left:0;top:2340px;width:1200px;height:264px;background:var(--band);border-top:1px solid #6a4214;border-bottom:1px solid #6a4214}
.touch h2{position:absolute;left:139px;top:74px;font:400 36px "Cinzel",serif;letter-spacing:4px;color:var(--cream)}
.touch .silhouette{right:70px;top:0;width:240px;height:264px;background:radial-gradient(ellipse at 55% 55%,#5f3a10 0%,#55330e 50%,transparent 72%)}
.partners{position:absolute;left:139px;top:168px;display:flex;align-items:center;gap:34px;font:600 18px "Open Sans",sans-serif;color:#fff}
.partners span{display:flex;align-items:center;gap:8px}
.partners b{display:block;width:14px;height:14px;background:#fff}

/* footer nav */
.footer-nav{left:0;top:2616px;width:1200px;height:72px;background:#2b1707}
.socials{position:absolute;left:178px;top:23px;display:flex;gap:14px}
.socials i{display:block;width:32px;height:32px;background:#4a2c11}
.footer-links{position:absolute;left:618px;top:25px;display:flex;gap:26px;font-size:14px;color:#fff}

/* newsletter */
.newsletter{left:521px;top:2744px;display:flex;align-items:center;gap:16px}
.newsletter h3{font:400 31px "Ubuntu",sans-serif;color:#fff;margin-right:4px}
.field{background:var(--input);border:1px solid #d8c9a3;color:#4a4a4a;font-size:13px;padding:0 8px;display:flex;align-items:center}
.btn{background:var(--yellow);color:#2b1707;font-size:13px;display:flex;align-items:center;justify-content:center}

/* footer cols */
.col-title{font:500 21px "Ubuntu",sans-serif;color:#fff}
.gallery{left:154px;top:2940px;width:210px;display:grid;grid-template-columns:1fr 1fr;gap:6px}
.gallery i{display:block;height:74px;background:linear-gradient(150deg,#8a5a2c,#3a1f0c 60%,#b07a3c)}
.tweet{left:398px;top:2935px;width:190px;font-size:15px;line-height:24px;color:#fff}
.tweet .hl{color:var(--gold)}
.tweet .when{font-size:10px;color:var(--gold);margin-top:16px}
.vids{left:638px;top:2938px;width:200px;display:flex;flex-direction:column;gap:18px}
.vids .item{display:flex;gap:10px;font-size:10px;line-height:13px;color:#fff}
.vids i{display:block;flex:0 0 38px;height:38px;background:linear-gradient(150deg,#a06a2a,#3a1f0c)}
.contact-form{left:892px;top:2940px;width:200px;display:flex;flex-direction:column;gap:10px}
.contact-form .field{height:24px;font-size:11px}
.copyright{left:139px;top:3194px;font-size:13px;color:var(--gold)}
</style>
</head>
<body>

<header class="abs site-header">
  <div class="abs brand"><span class="brand-mark"></span>Lena Hartwell</div>
  <nav class="abs main-nav">
    <a class="current" href="#">Home</a>
    <a href="#">Events</a><a href="#">Music</a><a href="#">Video</a><a href="#">Picture</a>
    <a class="pill" href="#">About</a>
    <a href="#">Discography</a><a href="#">Contacts</a>
  </nav>
</header>

<section class="abs hero">
  <div class="ph hero-photo" role="img" aria-label="Portrait of the singer in profile with a large drop earring, in warm gold tones"></div>
  <p class="abs hero-kicker" style="top:66px">THE SOUL OF MUSIC</p>
  <h1 class="abs hero-title" style="top:108px;font-weight:300">Lena Hartwell</h1>
  <p class="abs hero-copy" style="top:190px">With a powerfully unique voice and a definitive sound, Lena Hartwell consistently delivers soul stirring performances that captivate audiences around the world. Using her past as a spring board, Lena channels memories into melodies that are proud and strong.</p>
  <div class="abs hero-arrows" style="top:420px">
    <svg width="14" height="18" viewBox="0 0 14 18"><path d="M11 2 3 9l8 7" fill="none" stroke="#3a2108" stroke-width="3"/></svg>
    <svg width="14" height="18" viewBox="0 0 14 18"><path d="M3 2l8 7-8 7" fill="none" stroke="#3a2108" stroke-width="3"/></svg>
  </div>
</section>

<article class="abs promo" style="left:154px">
  <h3>Lena Hartwell<br>Band</h3>
  <p>I'm so excited after two great shows in my hometown Houston, Texas.</p>
  <span class="go"><svg width="20" height="16" viewBox="0 0 20 16"><path d="M1 8h16M11 2l6 6-6 6" fill="none" stroke="#f3c300" stroke-width="3"/></svg></span>
</article>
<article class="abs promo" style="left:466px">
  <h3>Lena Hartwell<br>On <span>WaveShelf</span></h3>
  <p>I have to admit technology is not my strongest part.</p>
  <span class="go"><svg width="20" height="16" viewBox="0 0 20 16"><path d="M1 8h16M11 2l6 6-6 6" fill="none" stroke="#f3c300" stroke-width="3"/></svg></span>
</article>
<article class="abs promo" style="left:773px">
  <h3>Song of the<br>Week</h3>
  <p style="width:260px"><span style="color:var(--gold)">Lena Hartwell</span> - Brightside Allstars &amp; Lena Hartwell - Imagine</p>
  <div class="player">
    <svg width="40" height="12" viewBox="0 0 40 12"><path d="M0 6l6-5v10zM8 6l6-5v10zM20 1h4v10h-4zM27 1h4v10h-4z" fill="#fff"/></svg>
    <div class="bar"><span class="knob"></span></div>
  </div>
</article>

<h2 class="abs sec-title" style="left:173px;top:866px">Featured <em>Musician Stories</em></h2>
<div class="abs stories">
  <div class="ph badge"></div>
  <h4 class="abs story-title">Court Legends Red Carpet Gala</h4>
  <p class="abs story-copy">Hello Friends! I'm headlining the Court Legends Red Carpet Gala All Star Weekend Event.<br>"A Night Of A Thousand Stars" @ The Silverline Plaza Of Houston GreenwaySummer Pride on June 24th in Fort Lauderdale, Florida.</p>
  <div class="abs mini-arrows" style="right:16px;bottom:14px">
    <span><svg width="8" height="10" viewBox="0 0 8 10"><path d="M6 1 2 5l4 4" fill="none" stroke="#f3c300" stroke-width="2"/></svg></span>
    <span><svg width="8" height="10" viewBox="0 0 8 10"><path d="M2 1l4 4-4 4" fill="none" stroke="#f3c300" stroke-width="2"/></svg></span>
  </div>
</div>
<h2 class="abs sec-title" style="left:780px;top:866px">Vivace <em>Magazine</em></h2>
<div class="ph magazine" role="img" aria-label="Magazine cover featuring the singer, with cover headlines"></div>
<div class="abs rule"></div>

<section class="abs album-panel">
  <h2 class="abs sec-title" style="left:34px;top:48px;font-size:33px">New <em>Album</em></h2>
  <p class="abs album-copy">Lorem ipsum dolor sit amet, consectetur adipiscing elit. Proin non rhoncus dolor. Curabitur rhoncus convallis erat, a placerat risus posuere vestibulum.</p>
  <div class="abs mini-arrows" style="left:34px;top:338px">
    <span style="width:14px;height:14px"><svg width="6" height="8" viewBox="0 0 6 8"><path d="M5 1 1 4l4 3" fill="none" stroke="#f3c300" stroke-width="2"/></svg></span>
    <span style="width:14px;height:14px"><svg width="6" height="8" viewBox="0 0 6 8"><path d="M1 1l4 3-4 3" fill="none" stroke="#f3c300" stroke-width="2"/></svg></span>
  </div>
  <div class="abs album" style="left:259px">
    <div class="cover" role="img" aria-label="Album cover: singer wrapped in a yellow coat" style="background:linear-gradient(160deg,#e9c13a,#7a4f1c 55%,#2c1808)"></div>
    <p class="name">Shine on me</p>
    <div class="meta"><span>$ 29.00</span><span>★★★★★</span></div>
  </div>
  <div class="abs album" style="left:485px">
    <div class="cover" role="img" aria-label="Album cover: singer portrait against a teal backdrop" style="background:linear-gradient(160deg,#3c8c86,#b39b7a 50%,#4a2e1a)"></div>
    <p class="name">My love can take......</p>
    <div class="meta"><span>$ 29.00</span><span>★★★★★</span></div>
  </div>
  <div class="abs album" style="left:711px">
    <div class="cover" role="img" aria-label="Album cover: Winter Glide skating show artwork in blue and yellow" style="background:linear-gradient(160deg,#1f4fb0,#2a86d8 45%,#e6c02a)"></div>
    <p class="name">Coastline Dreaming</p>
    <div class="meta"><span>$ 29.00</span><span>★★★★★</span></div>
  </div>
</section>

<h2 class="abs sec-title" style="left:154px;top:1640px">Latest <em>Events</em></h2>
<div class="abs mini-arrows" style="left:546px;top:1646px">
  <span><svg width="8" height="10" viewBox="0 0 8 10"><path d="M6 1 2 5l4 4" fill="none" stroke="#f3c300" stroke-width="2"/></svg></span>
  <span><svg width="8" height="10" viewBox="0 0 8 10"><path d="M2 1l4 4-4 4" fill="none" stroke="#f3c300" stroke-width="2"/></svg></span>
</div>
<div class="ph event-img" role="img" aria-label="Singer performing on stage under spotlights"></div>
<div class="abs event-text">
  <h4>Regent's Palace</h4>
  <p>Lorem ipsum dolor sit amet, consectetur adipiscing elit. Proin non rhoncus dolor. Curabitur rhoncus convallis erat, a placerat risus posuere vestibulum.</p>
  <p class="tix"><svg width="10" height="10" viewBox="0 0 10 10"><rect x="1" y="2" width="8" height="6" fill="none" stroke="#eeb515"/></svg>Buy Tickets</p>
</div>

<h2 class="abs sec-title" style="left:610px;top:1640px">Upcoming <em>Events</em></h2>
<div class="ph upcoming" role="img" aria-label="Event banner with a portrait of the singer on the right">
  <span class="date">FRI JAN 10, 2014 - 8:00 PM</span>
  <span class="who">Lena Hartwell</span>
  <span class="fan">Fanpage</span>
  <span class="with">With Nora Vandermeer</span>
  <span class="venue">Regent's Palace<br>Atlantic City, NJ</span>
</div>

<div class="abs video-head">
  <span class="ico"><svg width="14" height="16" viewBox="0 0 14 16"><path d="M2 1l11 7-11 7z" fill="#3a7fd0"/></svg></span>
  Watch the New Video Clip!
</div>
<div class="ph video-frame" role="img" aria-label="Video still of the singer performing with a microphone">
  <div class="abs play"><svg width="34" height="40" viewBox="0 0 34 40"><path d="M6 4l22 16L6 36" fill="none" stroke="#fff" stroke-width="7"/></svg></div>
</div>

<aside class="abs widget">
  <h3>Circlebook Widget</h3>
  <div class="find">Find us on Circlebook</div>
  <div class="profile">
    <div class="avatar"></div>
    <div><p class="pname">Lena Hartwell</p><span class="like">Like</span> <span class="like">138</span></div>
  </div>
  <div class="sep"></div>
  <div class="fans"><i></i><i></i><i></i><i></i></div>
</aside>

<section class="abs touch">
  <div class="ph silhouette" role="img" aria-label="Faint silhouette of a singer holding a microphone"></div>
  <h2>GET IN TOUCH</h2>
  <div class="partners">
    <span><b></b>Walnut Row Entertainment</span>
    <span>TuneBidder</span>
    <span>ClipStream</span>
    <span>Snapfolio</span>
    <span>EchoNation</span>
    <span>WaveShelf</span>
  </div>
</section>

<nav class="abs footer-nav">
  <div class="socials"><i></i><i></i><i></i><i></i><i></i></div>
  <div class="footer-links"><span>Home</span><span>Music</span><span>Video</span><span>Picture</span><span>About</span><span>Discography</span></div>
</nav>

<div class="abs newsletter">
  <h3>Newsletter</h3>
  <div class="field" style="width:257px;height:30px">Enter your Email</div>
  <div class="btn" style="width:96px;height:30px">Subscribe</div>
</div>

<h3 class="abs col-title" style="left:154px;top:2888px">Gallery</h3>
<div class="abs gallery" role="img" aria-label="Four thumbnail photos of the singer on stage and at events"><i></i><i></i><i></i><i></i></div>

<h3 class="abs col-title" style="left:398px;top:2888px">Latest Tweet</h3>
<div class="abs tweet">
  <p class="hl">With Nora Vandermeer</p>
  <p>with Nora Vandermeer Regent's Palace<br>Atlantic City, NJ</p>
  <p class="when">FRI JAN 10, 2014 - 8:00 PM</p>
</div>

<h3 class="abs col-title" style="left:638px;top:2888px">Latest Video</h3>
<div class="abs vids">
  <div class="item"><i></i><p>Lorem ipsum dolor sit amet, consectetur adipiscing elit. Nunc in felis arcu.</p></div>
  <div class="item"><i></i><p>Lorem ipsum dolor sit amet, consectetur adipiscing elit. Nunc in felis arcu.</p></div>
  <div class="item"><i></i><p>Lorem ipsum dolor sit amet, consectetur adipiscing elit. Nunc in felis arcu.</p></div>
</div>

<h3 class="abs col-title" style="left:900px;top:2888px">Contact</h3>
<form class="abs contact-form">
  <div class="field">Name</div>
  <div class="field">Last Name</div>
  <div class="field">Email</div>
  <div class="btn" style="width:70px;height:24px;align-self:flex-end">Submit</div>
</form>

<p class="abs copyright">© 2013 - All Rights Reserved.</p>

</body>
</html>
```